Tri-fold flyer for Managed Services IT company

We need a tri-fold flyer design for our Managed Services IT company. Our website is here: https://pelicanfjordit.net. While we don't have to match our website we do want to incorporate the logo in the flyer. We would like a flyer that is *very* easy and quick to read/skim over and convey our message. Something like these:

https://www.artkestrel.com/design/58203917

https://47sketchyard.com/postcard-flyer-design/contests/create-lead-generating-flyer-postcard-managed-services-company-815243

http://www.marbleoaksystems.com/managed-services-no-cost-one-month/

Target Market(s)

Business to business IT services

Industry/Entity Type

It Service

Font styles to use
Serif
Sans Serif

Requirements
Must have
• *very* easy and quick to read/skim over and convey our message
Should not have
• verbose, lots of text

```html
<!DOCTYPE html>
<html lang="en">
<head>
<meta charset="utf-8">
<title>Pelican Fjord – Tri-fold Outside</title>
<link href="https://fonts.googleapis.com/css2?family=Open+Sans:ital,wght@0,300;0,400;0,600;0,700;0,800;1,400;1,600&display=swap" rel="stylesheet">
<style>
  :root {
    --backdrop: #9c9c9c;
    --paper: #fbfbfb;
    --strip: #ececef;
    --brand-blue: #1f3f8f;
    --brand-orange: #e07a10;
    --ink: #1c1c1c;
    --muted: #444a55;
    --fold: rgba(0,0,0,0.06);
  }
  * { box-sizing: border-box; margin: 0; padding: 0; }
  html, body { width: 1200px; height: 800px; overflow: hidden; }
  body {
    background: var(--backdrop);
    font-family: "Open Sans", Arial, sans-serif;
    position: relative;
  }
  .brochure {
    position: absolute;
    left: 105px; top: 17px;
    width: 990px; height: 766px;
    background: var(--paper);
    box-shadow: 0 6px 24px rgba(0,0,0,0.25);
    overflow: hidden;
  }
  .contact-strip {
    position: absolute; left: 400px; width: 190px; top: 0; bottom: 0;
    background: var(--strip);
  }
  .panel {
    position: absolute; top: 0; height: 100%; width: 330px;
  }
  .panel--left { left: 0; }
  .panel--middle { left: 330px; }
  .panel--right { left: 660px; }
  .fold-line { position: absolute; top: 0; bottom: 0; width: 1px; background: var(--fold); }
  .fold-line--a { left: 330px; }
  .fold-line--b { left: 660px; }

  .wave { position: absolute; left: 0; top: 0; width: 990px; height: 766px; }

  /* Left panel */
  .intro-photo {
    position: absolute; left: 84px; top: 30px; width: 124px; height: 92px;
    border: 3px solid var(--brand-orange);
    background: linear-gradient(160deg, #c9c9c9, #8d8f93 60%, #5a5c62);
  }
  .intro-title {
    position: absolute; left: 40px; top: 136px;
    color: var(--brand-blue); font-weight: 700; font-size: 11px; font-style: italic;
  }
  .intro-lead {
    position: absolute; left: 40px; top: 156px; width: 250px;
    font-size: 8px; font-style: italic; color: var(--muted);
  }
  .intro-body {
    position: absolute; left: 40px; top: 176px; width: 255px;
    font-size: 8.5px; line-height: 1.45; font-style: italic; color: var(--muted);
  }
  .careers-note {
    position: absolute; left: 30px; top: 600px; width: 190px;
    color: var(--brand-blue); font-size: 9.5px; font-weight: 600; font-style: italic; line-height: 1.35;
  }
  .team-photo {
    position: absolute; left: 20px; top: 640px; width: 220px; height: 96px;
    background: linear-gradient(180deg, #f3f3f3 0%, #c9ccd3 35%, #3a4150 75%, #2a2f3a 100%);
  }

  /* Middle panel */
  .contact {
    position: absolute; left: 70px; width: 190px; text-align: center;
    color: var(--ink); font-weight: 700; font-size: 9.5px; line-height: 1.45;
  }
  .contact svg { display: block; margin: 0 auto 4px; }
  .contact--address { top: 70px; }
  .contact--phone { top: 150px; }
  .contact--web { top: 690px; font-size: 11px; }

  /* Right panel */
  .brand-name {
    position: absolute; left: 40px; top: 150px; width: 260px; text-align: center;
    color: var(--brand-blue); font-weight: 400; font-size: 26px; letter-spacing: 3px;
  }
  .cta { position: absolute; left: 40px; top: 626px; width: 270px; }
  .cta__line { display: block; line-height: 1.05; }
  .cta__line--strong { color: var(--brand-blue); font-weight: 800; font-size: 25px; }
  .cta__line--light { color: var(--brand-blue); font-weight: 300; font-size: 28px; }
  .cta__line--accent { color: var(--brand-orange); font-weight: 800; font-size: 25px; }
  .cta__body { margin-top: 6px; color: var(--ink); font-weight: 600; font-size: 13px; line-height: 1.35; }
</style>
</head>
<body>
<main class="brochure">
  <div class="contact-strip"></div>

  <svg class="wave" viewBox="0 0 990 766" xmlns="http://www.w3.org/2000/svg">
    <defs>
      <linearGradient id="techGlow" x1="0" y1="0" x2="1" y2="0">
        <stop offset="0" stop-color="#22344f"/>
        <stop offset="0.35" stop-color="#3f6fa8"/>
        <stop offset="0.6" stop-color="#7d9ac0"/>
        <stop offset="1" stop-color="#c9d1dc"/>
      </linearGradient>
    </defs>
    <path fill="var(--brand-blue)" d="M0,330 C200,250 450,270 620,222 C760,182 880,222 990,320 L990,420 L0,420 Z"/>
    <path fill="var(--brand-orange)" d="M990,466 C930,566 820,608 700,598 C600,590 520,644 420,644 C300,644 150,566 0,458 L0,420 L990,420 Z"/>
    <path role="img" aria-label="Photo of a person working at a computer surrounded by glowing digital data graphics" fill="url(#techGlow)"
      d="M0,360 C200,280 450,300 620,252 C760,212 880,252 990,350 L990,440 C930,542 820,584 700,574 C600,566 520,620 420,620 C300,620 150,546 0,434 Z"/>
  </svg>

  <div class="fold-line fold-line--a"></div>
  <div class="fold-line fold-line--b"></div>

  <section class="panel panel--left">
    <div class="intro-photo" role="img" aria-label="Photo of a businessperson holding a card with a question mark"></div>
    <h2 class="intro-title">WHO ARE WE?</h2>
    <p class="intro-lead">It's Nice To Know Who You're Working With, We Get That</p>
    <p class="intro-body">Pelican Fjord understands that making a decision means putting your trust in us. We encourage you to find out more about our company and read testimonials from our many satisfied customers!</p>
    <p class="careers-note">We are always looking for talented new people to join our team!</p>
    <div class="team-photo" role="img" aria-label="Group photo of the company team standing together"></div>
  </section>

  <section class="panel panel--middle">
    <div class="contact contact--address">
      <svg width="14" height="16" viewBox="0 0 14 16"><path d="M7 1a5 5 0 0 1 5 5c0 4-5 9-5 9S2 10 2 6a5 5 0 0 1 5-5z" fill="none" stroke="var(--brand-blue)" stroke-width="1.4"/><circle cx="7" cy="6" r="1.8" fill="var(--brand-blue)"/></svg>
      2280 Harbor Row, Suite 310<br>Lakeview, MN 55012
    </div>
    <div class="contact contact--phone">
      <svg width="16" height="16" viewBox="0 0 16 16"><circle cx="8" cy="8" r="7" fill="none" stroke="var(--brand-blue)" stroke-width="1.3"/><path d="M5.5 4.5l1.3 1.6-.7 1c.5 1 1.3 1.8 2.3 2.3l1-.7 1.6 1.3-.8 1.2c-2.6-.4-4.8-2.6-5.2-5.2z" fill="var(--brand-blue)"/></svg>
      555-014-2871
    </div>
    <div class="contact contact--web">
      <svg width="16" height="16" viewBox="0 0 16 16"><g fill="none" stroke="var(--brand-blue)" stroke-width="1.2"><circle cx="8" cy="8" r="7"/><ellipse cx="8" cy="8" rx="3" ry="7"/><path d="M1 8h14M2.5 4.5h11M2.5 11.5h11"/></g></svg>
      www.pelicanfjordit.net
    </div>
  </section>

  <section class="panel panel--right">
    <div class="brand-name">PELICAN FJORD</div>
    <div class="cta">
      <h1>
        <span class="cta__line cta__line--strong">PREFER TO SPEAK</span>
        <span class="cta__line cta__line--light">FACE TO FACE?</span>
        <span class="cta__line cta__line--accent">WE DO TOO.</span>
      </h1>
      <p class="cta__body">Let's get in touch for a one-on-one discussion about your IT.</p>
    </div>
  </section>
</main>
</body>
</html>
```